依頼詳細
PCとスマホデザインの両方納品をいただきますが、
まずはデザインイメージが確認しやすいPCページのみの提案をお願いします。
スマホページは当選者に納品時にお願いしたいと思います。
スマホサイズについて、表示は横幅375pxで作成し、
デザインデータは2倍の横幅750pxのカンバスサイズで作成してください。
(Retinaディスプレイに対応するため)
レスポンシブウェブデザインを意識したデザインでお願いします。

■サイトマップ
添付の画面遷移図をご確認ください。

■参考サイト
http://hoshizora-tetsuko.co.jp/

■内容について
鋳造部品等を製作する会社のサイトリニューアルになります。
既存サイト
http://www.senbeiseiko.com/kiyora/index.html

■素材写真
画像データについては、フリー素材から流用して
イメージ画像に当て込んでください。
足りない場合は、一旦他のサイトの写真をサンプルとして
入れてください。(サンプルなどの表記をお願いします)
また、購入が必要な写真などを利用した場合、
価格とサイト名を教えてください。

また、Lumera Photosで定期契約をしていますので、
Lumera Photosの画像は使用できます。
デザイン時はカンプ画像をお入れいただきますようお願いします。

■ワイヤーフレーム
https://mock.wirevista.net/view/1a2b3c4d-5e6f-4a7b-8c9d-0e1f2a3b4c5d-8812/?fullscreen
コンテンツの構成としてワイヤーフレームを作成しましたが
必ずしもワイヤーフレームの通りではなくて大丈夫です。
TOPページに配置するコンテンツを見ていただき、デザインは
デザイナーの皆様におまかせしたいと思います。

----------------------------------------------------------------------------
【制作物に対するお願い】

■フォントについて
・無料で使えるフォントで作成をお願いします。
・OSに紐づくフォントの使用は控えていただければと思います (ヒラギノなど)

ページ数
1ページ
希望イメージ
シンプル 複雑
単色 カラフル
暗い 明るい
日常 高級
遊び心 厳粛
未来的 伝統的
女性的 男性的
希望する色
アクセントカラー:茶色、もしくは青色
納品ファイル
• 高解像度JPG (.jpg)
• イラストレーター形式 (.ai)
• フォトショップ形式 (.psd)
補足説明
上記のいずれか1つ(アウトラインありとなしの2つ)と高解像度JPGを納品お願いします。
adobe XDでの納品も可能です。

```html
<!DOCTYPE html>
<html lang="ja">
<head>
<meta charset="utf-8">
<title>星川伸銅株式会社</title>
<link rel="stylesheet" href="https://fonts.googleapis.com/css2?family=Montserrat:wght@500;600;700;800&family=Noto+Sans+JP:wght@400;500;700&display=swap">
<style>
:root{
  --blue:#2340b5;
  --blue-deep:#1a2f8f;
  --ink:#1b1d2b;
  --muted:#555a6b;
  --pale:#f3f5fb;
  --line:#e4e8f3;
  --white:#ffffff;
  --footer:#262626;
}
*{margin:0;padding:0;box-sizing:border-box}
html,body{width:1200px;height:5052px;overflow:hidden}
body{position:relative;background:var(--white);color:var(--ink);font-family:"Noto Sans JP",sans-serif}
.abs{position:absolute}
.en{font-family:"Montserrat",sans-serif}
.grid-bg{position:absolute;left:0;top:800px;width:1200px;height:3780px;background:
  linear-gradient(90deg,transparent 0 399px,var(--line) 399px 400px,transparent 400px 799px,var(--line) 799px 800px,transparent 800px);}
.pale-band{position:absolute;left:0;width:1200px;background:var(--pale)}

/* header */
.site-header{position:absolute;left:0;top:0;width:1200px;height:80px;background:var(--white)}
.brand{position:absolute;left:20px;top:26px;font-size:20px;font-weight:700;letter-spacing:.05em}
.nav{position:absolute;right:200px;top:32px;display:flex;gap:30px;font-size:13px;font-weight:500;white-space:nowrap}
.btn-contact{position:absolute;right:20px;top:22px;width:150px;height:40px;background:var(--blue);color:#fff;font-size:13px;font-weight:500;display:flex;align-items:center;justify-content:center;border-radius:2px;white-space:nowrap}

/* hero */
.hero-blue{position:absolute;left:0;top:80px;width:1000px;height:700px;background:var(--blue)}
.hero-photo{position:absolute;left:180px;top:80px;width:1020px;height:560px;background:linear-gradient(120deg,#3f5a52 0%,#6f8a6a 35%,#2c3330 60%,#a65a28 80%,#2a2c30 100%)}
.hero-title{position:absolute;left:80px;top:290px;color:#fff;font-size:56px;font-weight:700;line-height:1.4;letter-spacing:.06em;white-space:nowrap}
.hero-vertical{position:absolute;left:150px;top:350px;color:#fff;font-size:12px;letter-spacing:.2em;writing-mode:vertical-rl}
.hero-scroll{position:absolute;left:68px;top:520px;color:#fff;font-size:11px;letter-spacing:.25em;writing-mode:vertical-rl}
.dots{position:absolute;left:1070px;top:618px;display:flex;gap:10px}
.dots span{width:18px;height:3px;background:rgba(255,255,255,.5)}
.dots span:first-child{background:#fff}

/* section heads */
.label{font-family:"Montserrat",sans-serif;color:var(--blue);font-weight:700;font-size:22px;letter-spacing:.12em;display:flex;align-items:center;gap:14px;white-space:nowrap}
.label::after{content:"";width:28px;height:2px;background:var(--blue)}
.label.center::after{display:none}
.title{font-size:36px;font-weight:700;letter-spacing:.06em;white-space:nowrap}

.read-more{display:flex;align-items:center;gap:18px;font-family:"Montserrat",sans-serif;font-weight:700;font-size:18px;color:var(--blue-deep);letter-spacing:.06em;white-space:nowrap}
.arrow-circle{flex:none;width:40px;height:40px;border-radius:50%;background:var(--blue-deep);display:flex;align-items:center;justify-content:center}
.pill{background:#fff;border-radius:40px;box-shadow:0 6px 24px rgba(30,45,110,.12);padding:0 14px 0 32px;justify-content:space-between}

.ph{position:absolute}
.body-text{font-size:14px;line-height:2;color:var(--muted)}

.product-name{position:absolute;width:320px;text-align:center;font-size:18px;font-weight:700}
.product-text{position:absolute;width:320px;font-size:15px;line-height:1.85;letter-spacing:.02em}

.tech-card{position:absolute;left:700px;top:2512px;width:420px;height:352px;background:#fff;box-shadow:0 10px 30px rgba(30,45,110,.1);padding:40px 30px 0 40px}

.news-item{position:absolute;left:380px;width:740px;height:80px;display:flex;align-items:center;padding:0 24px 0 40px}
.news-date{font-family:"Montserrat",sans-serif;font-size:14px;font-weight:600;margin-bottom:6px}
.news-text{font-size:14px;white-space:nowrap}

.contact-box{position:absolute;left:80px;top:4420px;width:1040px;height:340px;background:var(--blue);overflow:hidden}
.contact-ghost{position:absolute;left:0;width:100%;top:24px;text-align:center;font-family:"Montserrat",sans-serif;font-weight:800;font-size:110px;letter-spacing:.15em;color:rgba(255,255,255,.08)}
.contact-lead{position:absolute;left:0;width:100%;top:112px;text-align:center;color:#fff;font-size:20px;font-weight:500;letter-spacing:.05em}
.contact-btn{position:absolute;top:172px;width:428px;height:120px;border:1px solid rgba(255,255,255,.6);background:rgba(255,255,255,.12);display:flex;align-items:center;gap:26px;padding-left:30px;color:#fff;white-space:nowrap}
.icon-box{flex:none;width:60px;height:60px;background:#fff;border-radius:6px;display:flex;align-items:center;justify-content:center}

.site-footer{position:absolute;left:0;top:4780px;width:1200px;height:272px;background:var(--footer);color:#fff}
.foot-nav{position:absolute;right:80px;top:88px;display:grid;grid-template-columns:repeat(5,auto);column-gap:40px;row-gap:20px;font-size:11px;color:#ddd;white-space:nowrap}
.copy{position:absolute;left:0;width:100%;top:216px;text-align:center;font-size:10px;color:#999;letter-spacing:.05em}
</style>
</head>
<body>

<div class="pale-band" style="top:800px;height:1450px"></div>
<div class="pale-band" style="top:2340px;height:580px;background:#f6f8fc"></div>
<div class="grid-bg"></div>

<header class="site-header">
  <div class="brand">星川伸銅株式会社</div>
  <nav class="nav"><span>会社概要</span><span>製造案内</span><span>製品紹介</span><span>採用情報</span></nav>
  <div class="btn-contact">お問い合わせ</div>
</header>

<section>
  <div class="hero-blue"></div>
  <div class="hero-photo" role="img" aria-label="鍛造工場で大型機械を操作する作業員と火花"></div>
  <h1 class="hero-title">鍛造技術に、<br>自信と誇りを持って</h1>
  <div class="hero-vertical en">Forging technology since 1950</div>
  <div class="hero-scroll en">SCROLL</div>
  <div class="dots"><span></span><span></span><span></span><span></span></div>
</section>

<section>
  <div class="abs label" style="left:80px;top:892px">ABOUT US</div>
  <h2 class="abs title" style="left:80px;top:936px">星川伸銅とは</h2>
  <div class="ph" style="left:80px;top:1020px;width:1040px;height:252px;background:linear-gradient(90deg,#2a1a10 0%,#c0702a 40%,#f2b050 55%,#9a4a1c 75%,#1e1410 100%)" role="img" aria-label="歯車を手で組み合わせるイメージ"></div>
  <p class="abs" style="left:80px;top:1326px;font-size:20px;font-weight:700">もの造りのプロとして、確かな技術でお応えします。</p>
  <p class="abs body-text" style="left:80px;top:1388px;width:700px">星川伸銅株式会社は創業以来七十年以上に渡り、鍛造品を製作してきました。<br>時代のニーズに応えつつ、これまで培ってきた職人の技を継承し、<br>社員全員一丸となって努力を重ね、質の高い技術・製品・サービスを常に目指します。</p>
  <div class="abs read-more pill" style="left:880px;top:1410px;width:240px;height:64px">READ MORE<span class="arrow-circle"><svg width="18" height="14" viewBox="0 0 18 14"><path d="M1 7h15M10 1l6 6-6 6" stroke="#fff" stroke-width="2.4" fill="none"/></svg></span></div>
</section>

<section>
  <div class="abs label" style="left:80px;top:1656px">PRODUCT</div>
  <h2 class="abs title" style="left:80px;top:1700px">製品紹介</h2>
  <div class="ph" style="left:80px;top:1784px;width:320px;height:204px;background:linear-gradient(135deg,#5a3a26,#c07a48 50%,#3a2a20)" role="img" aria-label="機械部品の写真"></div>
  <div class="ph" style="left:440px;top:1784px;width:320px;height:204px;background:linear-gradient(135deg,#1e3a2a,#3f7a56 50%,#18261e)" role="img" aria-label="電子基板の写真"></div>
  <div class="ph" style="left:800px;top:1784px;width:320px;height:204px;background:linear-gradient(135deg,#2a2a2a,#8a8a8a 50%,#222)" role="img" aria-label="金属歯車の写真"></div>
  <div class="product-name" style="left:80px;top:2010px">機械部品</div>
  <div class="product-name" style="left:440px;top:2010px">電気部品</div>
  <div class="product-name" style="left:800px;top:2010px">その他の部品</div>
  <p class="product-text" style="left:80px;top:2054px">テキストテキストテキストテキストテキストテキストテキストテキストテキストテキストテキストテキストテキスト</p>
  <p class="product-text" style="left:440px;top:2054px">テキストテキストテキストテキストテキストテキストテキストテキストテキストテキストテキストテキストテキスト</p>
  <p class="product-text" style="left:800px;top:2054px">テキストテキストテキストテキストテキストテキストテキストテキストテキストテキストテキストテキストテキスト</p>
</section>

<section>
  <div class="abs label" style="left:80px;top:2384px">TECHNOLOGY</div>
  <h2 class="abs title" style="left:80px;top:2428px">製造案内</h2>
  <div class="ph" style="left:80px;top:2512px;width:620px;height:352px;background:linear-gradient(160deg,#2a1a14 0%,#8a2a14 40%,#f07a20 60%,#3a1e14 100%)" role="img" aria-label="溶けた金属を流し込む鋳造作業"></div>
  <div class="tech-card">
    <p style="font-size:20px;font-weight:700;line-height:1.6">充実した設備と確かな技術で<br>お客様のご要望に応えます。</p>
    <p class="body-text" style="margin-top:14px;font-size:13px;line-height:1.9">星川伸銅株式会社は、自動化生産ラインで品質の高い製品を、これまで培ってきた技術で製造しております。お客様のご要望に応じて、小ロットから大型製品まで幅広く対応します。</p>
  </div>
  <div class="abs read-more pill" style="left:860px;top:2770px;width:240px;height:64px">READ MORE<span class="arrow-circle"><svg width="18" height="14" viewBox="0 0 18 14"><path d="M1 7h15M10 1l6 6-6 6" stroke="#fff" stroke-width="2.4" fill="none"/></svg></span></div>
</section>

<section>
  <div class="abs label center" style="left:0;width:1200px;top:3056px;justify-content:center">RECRUIT</div>
  <h2 class="abs title" style="left:0;width:1200px;top:3100px;text-align:center">採用情報</h2>
  <div class="ph" style="left:80px;top:3180px;width:1040px;height:420px;background:linear-gradient(90deg,#2a3850 0%,#4a5a70 35%,#7a6a50 60%,#3a4a60 100%)" role="img" aria-label="ヘルメットを着用した作業員たちの写真"></div>
  <div class="ph" style="left:80px;top:3180px;width:1040px;height:420px;background:rgba(15,25,60,.45)"></div>
  <p class="abs" style="left:0;width:1200px;top:3308px;text-align:center;color:#fff;font-size:28px;font-weight:700">星川伸銅ではともに働く仲間を募集しています。</p>
  <p class="abs" style="left:0;width:1200px;top:3380px;text-align:center;color:#fff;font-size:14px;line-height:2">星川伸銅株式会社は、製造業の現場で常に挑戦し、技術を磨き続けています。<br>お客様の様々なご要望にお応えするべく、ともに働く仲間を募集しています。<br>当社で新しい一歩を踏み出したい方、未経験者でも一から指導します。ご応募をお待ちしております。</p>
</section>

<section>
  <div class="abs label" style="left:80px;top:3896px">NEWS</div>
  <h2 class="abs title" style="left:80px;top:3940px">お知らせ</h2>
  <div class="abs read-more" style="left:80px;top:4040px">READ MORE<span class="arrow-circle"><svg width="18" height="14" viewBox="0 0 18 14"><path d="M1 7h15M10 1l6 6-6 6" stroke="#fff" stroke-width="2.4" fill="none"/></svg></span></div>

  <div class="news-item pill" style="top:3900px"><div><div class="news-date">2021.10.08</div><div class="news-text">テキストテキストテキストテキストテキストテキストテキストテキスト</div></div><svg width="22" height="18" viewBox="0 0 22 18"><path d="M1 9h19M13 2l7 7-7 7" stroke="#2340b5" stroke-width="2.4" fill="none"/></svg></div>
  <div class="news-item pill" style="top:4008px"><div><div class="news-date">2021.10.08</div><div class="news-text">テキストテキストテキストテキストテキストテキストテキストテキスト</div></div><svg width="22" height="18" viewBox="0 0 22 18"><path d="M1 9h19M13 2l7 7-7 7" stroke="#2340b5" stroke-width="2.4" fill="none"/></svg></div>
  <div class="news-item pill" style="top:4116px"><div><div class="news-date">2021.10.08</div><div class="news-text">テキストテキストテキストテキストテキストテキストテキストテキスト</div></div><svg width="22" height="18" viewBox="0 0 22 18"><path d="M1 9h19M13 2l7 7-7 7" stroke="#2340b5" stroke-width="2.4" fill="none"/></svg></div>
  <div class="news-item pill" style="top:4224px"><div><div class="news-date">2021.10.08</div><div class="news-text">テキストテキストテキストテキストテキストテキストテキストテキスト</div></div><svg width="22" height="18" viewBox="0 0 22 18"><path d="M1 9h19M13 2l7 7-7 7" stroke="#2340b5" stroke-width="2.4" fill="none"/></svg></div>
</section>

<section class="contact-box">
  <div class="contact-ghost">CONTACT</div>
  <p class="contact-lead">ご質問や ご相談を承ります。どうぞ、お気軽にお問い合わせください。</p>
  <div class="contact-btn" style="left:60px">
    <span class="icon-box"><svg width="28" height="28" viewBox="0 0 24 24"><path d="M6.6 10.8a15 15 0 0 0 6.6 6.6l2.2-2.2a1 1 0 0 1 1-.25 11.4 11.4 0 0 0 3.6.57 1 1 0 0 1 1 1V20a1 1 0 0 1-1 1A17 17 0 0 1 3 4a1 1 0 0 1 1-1h3.5a1 1 0 0 1 1 1c0 1.25.2 2.45.57 3.57a1 1 0 0 1-.25 1z" fill="#2340b5"/></svg></span>
    <div><div style="font-size:28px;font-weight:700" class="en"><span style="font-size:14px;margin-right:10px">TEL.</span>03-5555-0182</div><div style="font-size:11px;margin-top:4px">受付時間：8:30〜17:30（土日祝除く）</div></div>
  </div>
  <div class="contact-btn" style="left:552px">
    <span class="icon-box"><svg width="28" height="22" viewBox="0 0 28 22"><rect x="1" y="1" width="26" height="20" rx="2" fill="none" stroke="#2340b5" stroke-width="2.4"/><path d="M2 3l12 9 12-9" fill="none" stroke="#2340b5" stroke-width="2.4"/></svg></span>
    <div style="font-size:22px;font-weight:700">メールでのお問い合わせ</div>
  </div>
</section>

<footer class="site-footer">
  <div class="abs" style="left:80px;top:100px;font-size:24px;font-weight:700;letter-spacing:.05em">星川伸銅株式会社</div>
  <nav class="foot-nav">
    <span>トップページ</span><span>会社概要</span><span>製造案内</span><span>製品紹介</span><span>採用情報</span>
    <span>お知らせ</span><span>お問い合わせ</span><span>プライバシーポリシー</span><span>サイトマップ</span><span>アクセス</span>
  </nav>
  <p class="copy">Copyright © 2021 Hoshikawa Shindo Co.,Ltd. All Rights Reserved.</p>
</footer>

</body>
</html>
```